DESIGN FOR FLAVOURED CORDIAL LABEL SUITABLE FOR LOCAL AND EXPORTING COUNTERIES

UPDATED BRIEF ON NUMBER 7
This cordial manufactured in Malaysia, belongs to the same product category as Velmora and Torvix. Feedback has suggested that the current Kolra label lacks visual appeal, prompting us to embark on a redesign that enhances visibility and draws consumer attention on store shelves—both locally and internationally.

Key design requirements:
1- The concept should be versatile enough to accommodate various flavors, including Mango, Orange, Grape, Sarsi, Lychee, Rose, and Pineapple, while maintaining a cohesive brand identity.
2- All essential product information must be incorporated, ensuring clarity and compliance with both local and international labeling regulations for export markets.
3- Designers are encouraged to explore creative approaches to make the label visually striking, culturally adaptable, and appealing across diverse consumer demographics.
4- The brand logo may be presented in either white or red, depending on what best suits the overall design while maintaining strong brand recognition in global markets.
5- You may refer to our current label for your perusal.
6- The redesigned label must follow the same artwork dimensions as the existing version. We include the cordial bottle image for your illustration.
7- Real fruit images can be used on label

https://files.plimbox.example/file/d/8qLmZxTbWn4cRv2HsKdJ7pYfGu3eNaV0/view?usp=share_link

Target Market(s)

Malaysia, Archipelago, Middle East, African counteries

Industry/Entity Type

Beverage

Font styles to use
Other font styles liked:
• any fonts suitable but not too fancy.

Requirements
Must have
• Info like in artworks
Nice to have
• creative approaches to visually represent the flavor through design elements such as color palettes, abstract patterns, typography, and symbolic imagery other than pictorial fruits/ graphical fruit

```html
<!DOCTYPE html>
<html lang="en">
<head>
<meta charset="utf-8">
<title>Kolra Grape Flavoured Cordial Label</title>
<link rel="stylesheet" href="https://fonts.googleapis.com/css2?family=Nunito+Sans:wght@400;700;800;900&display=swap">
<style>
  :root {
    --bg: #e6e6e6;
    --label-top: #fbfafc;
    --label-mid: #ddd0e4;
    --label-low: #a987b6;
    --label-base: #8a5c9a;
    --navy: #2e3459;
    --brand-red: #e2382f;
    --white: #ffffff;
    --leaf: #5fa23a;
    --grape: #3a2f5a;
    --icon-ring: #7a4e8a;
  }
  * { box-sizing: border-box; margin: 0; padding: 0; }
  html, body { width: 1200px; height: 815px; overflow: hidden; }
  body {
    background: var(--bg);
    font-family: "Nunito Sans", sans-serif;
    position: relative;
  }
  .label {
    position: absolute;
    left: 100px; top: 170px;
    width: 1000px; height: 475px;
    background: linear-gradient(180deg, var(--label-top) 0%, var(--label-top) 30%, var(--label-mid) 60%, var(--label-low) 85%, var(--label-base) 100%);
    border-radius: 6px;
    box-shadow: 0 2px 10px rgba(0,0,0,0.08);
  }
  .brand {
    position: absolute; left: 0; right: 0; top: 28px;
    text-align: center;
  }
  .brand-name {
    display: inline-flex; align-items: center; gap: 8px;
    color: var(--brand-red); font-weight: 800; font-size: 42px; line-height: 1;
  }
  .brand-dot { width: 12px; height: 12px; border-radius: 50%; background: var(--brand-red); }
  .brand-since { display: block; font-size: 11px; font-weight: 700; color: var(--brand-red); margin-top: 2px; }
  .flavour {
    position: absolute; left: 0; right: 0; top: 88px;
    text-align: center; color: var(--navy);
    font-weight: 900; font-size: 112px; line-height: 1; letter-spacing: 1px;
  }
  .product-type {
    position: absolute; left: 0; right: 0; top: 206px;
    display: flex; justify-content: center; align-items: center; gap: 14px;
    color: var(--navy); font-weight: 800; font-size: 34px;
  }
  .product-type .rule { width: 60px; height: 3px; background: var(--navy); }
  .product-type-fr {
    position: absolute; left: 0; right: 0; top: 252px;
    text-align: center; color: var(--navy);
    font-weight: 800; font-size: 20px; line-height: 1.2;
  }
  .fruit-visual {
    position: absolute; left: 285px; top: 305px;
    width: 420px; height: 160px;
    border-radius: 80px 80px 70px 70px;
    background:
      radial-gradient(ellipse 32% 70% at 68% 58%, var(--grape) 0%, #4b3d70 60%, rgba(75,61,112,0) 100%),
      radial-gradient(ellipse 30% 60% at 22% 40%, var(--leaf) 0%, #78b54f 60%, rgba(120,181,79,0) 100%),
      radial-gradient(ellipse 22% 55% at 92% 35%, #6daa42 0%, rgba(109,170,66,0) 100%);
  }
  .cert-badge {
    position: absolute; left: 34px; top: 330px;
    width: 56px; height: 56px; border-radius: 50%;
    background: var(--white); border: 3px solid var(--navy);
  }
  .cert-note {
    position: absolute; left: 20px; top: 392px; width: 84px;
    text-align: center; font-size: 9px; color: var(--navy); font-weight: 700;
  }
  .net-content {
    position: absolute; left: 60px; top: 432px;
    color: var(--white); font-weight: 800; font-size: 21px;
  }
  .facts {
    position: absolute; right: 40px; top: 220px;
    display: flex; flex-direction: column; align-items: center; gap: 6px;
  }
  .fact { display: flex; flex-direction: column; align-items: center; }
  .fact-ring {
    width: 34px; height: 34px; border-radius: 50%;
    border: 3px solid var(--icon-ring); background: var(--white);
    display: flex; align-items: center; justify-content: center;
    font-size: 11px; font-weight: 900; color: var(--icon-ring);
  }
  .fact-note { font-size: 8px; color: var(--navy); font-weight: 700; margin-top: 2px; }
  .jug { margin-top: 8px; text-align: center; }
  .jug-note { font-size: 10px; font-weight: 800; color: var(--white); margin-top: -30px; position: relative; }
</style>
</head>
<body>
  <section class="label">
    <div class="brand">
      <span class="brand-name"><span class="brand-dot"></span>Kolra</span>
      <span class="brand-since">Since 1978</span>
    </div>

    <h1 class="flavour">GRAPE</h1>
    <div class="product-type"><span class="rule"></span>Flavoured Cordial<span class="rule"></span></div>
    <p class="product-type-fr">Boisson Concentrée au Goût de Raisin<br>avec Édulcorant</p>

    <div class="fruit-visual" role="img" aria-label="Photograph of a bunch of dark grapes with green vine leaves"></div>

    <div class="cert-badge" aria-hidden="true"></div>
    <p class="cert-note">Certified halal</p>

    <p class="net-content">Net Content / Contenu Net: 840ml</p>

    <div class="facts">
      <div class="fact"><span class="fact-ring">~40</span><span class="fact-note">servings each</span></div>
      <div class="fact"><span class="fact-ring">1:8</span><span class="fact-note">dilute ratio</span></div>
      <div class="fact"><span class="fact-ring">0%</span><span class="fact-note">fat free</span></div>
      <div class="jug">
        <svg width="44" height="58" viewBox="0 0 44 58" aria-hidden="true">
          <path d="M8 4 H36 L34 12 Q42 24 40 50 Q40 56 34 56 H10 Q4 56 4 50 Q2 24 10 12 Z" fill="#6b1f3a" stroke="#ffffff" stroke-width="2"/>
          <path d="M8 4 H36" stroke="#ffffff" stroke-width="3"/>
        </svg>
        <p class="jug-note">makes 8lt</p>
      </div>
    </div>
  </section>
</body>
</html>
```